Create an awesome website for a medical clinic

This is a new website for a doctor's office. The site should be clean and modern, easy to navigate.

This is a wellness clinic, we want to help our clients have a healthy, active lifestyle. It should be friendly and inviting, and easy for them to call or schedule an appointment.

The site should be responsive and designed using the attached Bootstrap 3 PSD.

We will provide stock photos, until then please use stock photos from:

pictovault.net or
imagebarrow.net (preferred)

Some example sites of clean and modern designs that we like:

https://tarvelspine.example/
http://quellmarrow.example/
http://brisklyhale.example/

Also attached is a temporary logo you can use.

Reason: Thank you everyone for your great designs - we need a little more time so I'm extending the project.

Need extra days to review

Also, the colors in the new logo I just linked to are the final colors of the logo, so feel free to use any complimentary colors to it.

Hi everyone, The boss wants to change the layout of the site a little bit - here's the revised layout: https://www.filecrate.example/s/k9pz31xq7vn84te/notes%2011_29_2017.pdf?dl=0 And the graphic assets you can use are here: https://www.filecrate.example/s/k9pz31xq7vn84te/notes%2011_29_2017.pdf?dl=0 Feel free to change the background color of the "topbar", and change the icons of the "why people trust us" if you want, these are just temporary placeholders. Thanks for your patience and hard work!

Target Market(s)

People seeking medical treatment (wellness clinic)

Industry/Entity Type

Doctor

Number of Pages Required

1 page

Font styles to use
Sans Serif

Colors
0592cd
33a6d7
abd037
9bcb3c

Requirements
Must have
• The home page should have: a strong hero image/slideshow, clinic phone number should be prominent and at the top of the page (in the nav), a "what to expect" section (this is like a FAQs section - see attachment), and a strong call to action (a button to call or schedule an appointment).
• The what to expect section is useful so that prospective clients can determine if we're a good fit for them or not. It's a basic, first-step pre-qualification block of information.
• Social media icons which links to our social media profiles should be included.
Nice to have
• - Link to 3 most recent blog entries
• - Testimonials
• - How a multilevel nav menu looks.

```html
<!DOCTYPE html>
<html lang="en">
<head>
<meta charset="utf-8">
<title>Fernly Medical Clinic</title>
<link href="https://fonts.googleapis.com/css2?family=Open+Sans:wght@400;600;700&display=swap" rel="stylesheet">
<style>
:root{
  --blue:#0592cd;
  --blue-light:#33a6d7;
  --green:#9bcb3c;
  --green-dark:#5aa02c;
  --ink:#1f1f1f;
  --muted:#555;
  --gray-band:#d9d9d9;
  --dark-band:#2b2c2e;
  --white:#fff;
}
*{box-sizing:border-box;margin:0;padding:0}
html,body{width:1200px;height:4787px;overflow:hidden}
body{font-family:"Open Sans",Arial,sans-serif;color:var(--ink);background:var(--white);position:relative}
.wrap{width:1084px;margin:0 auto;position:relative}
.section-title{font-size:40px;font-weight:700;text-align:center;color:var(--ink)}
.btn{display:inline-block;background:var(--blue);color:var(--white);font-weight:700;font-size:15px;text-align:center;line-height:36px;height:36px;width:180px}
.photo{display:block}

/* top bar */
.topbar{height:38px;background:var(--blue);color:var(--white);font-size:14px;font-weight:600}
.topbar .wrap{display:flex;justify-content:space-between;align-items:center;height:38px}
.social{display:flex;gap:10px}
.social span{width:22px;height:22px;border-radius:50%;background:var(--white);opacity:.85}

/* header */
.header{height:144px}
.header .wrap{display:flex;align-items:center;height:144px}
.brand{color:var(--green-dark);font-weight:700;font-size:30px;line-height:34px;width:250px}
.brand small{display:block;font-size:20px;line-height:24px}
.nav{display:flex;gap:24px;font-size:15px;font-weight:700;color:var(--ink);margin-left:10px}
.cta{margin-left:auto;background:var(--blue);color:var(--white);font-weight:700;font-size:15px;padding:0 18px;height:44px;line-height:44px}

/* hero */
.hero{height:488px;position:relative;background:linear-gradient(90deg,#c9d3da 0%,#eef1f3 30%,#f4f6f8 55%,#d7e3ea 80%,#9fb8c8 100%)}
.hero-text{position:absolute;left:620px;top:82px;width:480px;text-align:center}
.hero-text h1{font-size:44px;font-weight:600;line-height:56px;color:var(--ink)}
.hero-text p{font-size:17px;line-height:26px;margin:30px auto 0;width:400px;color:#333}
.arrow{position:absolute;top:200px;width:40px;height:80px;background:rgba(120,120,120,.55);display:flex;align-items:center;justify-content:center}
.arrow.left{left:0}.arrow.right{right:0}

/* services */
.services{height:590px;padding-top:80px}
.service-row{display:flex;justify-content:space-between;margin-top:86px}
.service{width:262px;text-align:center}
.service-card{border:2px solid #e6e6e6;height:182px;margin-top:-60px;padding:70px 20px 0}
.service .icon{width:120px;height:120px;border-radius:50%;background:var(--blue);margin:0 auto;position:relative;z-index:1;display:flex;align-items:center;justify-content:center}
.service h3{font-size:18px;font-weight:700}
.service p{font-size:13px;line-height:18px;color:var(--muted);margin-top:10px;height:54px;overflow:hidden}
.service .btn{margin-top:32px}

/* expect */
.expect{height:623px;background:var(--gray-band);position:relative;padding-top:76px}
.faq{width:570px;margin-top:60px}
.faq h4{font-size:17px;font-weight:700;line-height:24px}
.faq p{font-size:13px;line-height:20px;color:var(--muted);margin:10px 0 34px}
.faq p:last-child{margin-bottom:0}
.expect .photo{position:absolute;left:670px;top:134px;width:430px;height:489px;background:linear-gradient(180deg,#e8e4e0,#f3f3f3 60%,#dfe6ec)}

/* blog */
.blog{height:836px;background:linear-gradient(180deg,#3a3b3d,var(--dark-band) 60%,#222);padding-top:72px}
.blog .section-title{color:var(--white)}
.blog-row{display:flex;justify-content:space-between;margin-top:110px}
.post{width:313px;height:511px;background:var(--white)}
.post .photo{height:204px;background:linear-gradient(135deg,#b9c4cc,#eaeef1 50%,#8ea2b1)}
.post-body{padding:30px 14px}
.post h3{font-size:19px;font-weight:700}
.post p{font-size:14px;line-height:22px;color:#333;margin-top:14px}
.post .more{display:block;color:var(--blue);font-weight:700;font-size:15px;margin-top:20px}

/* why */
.why{height:606px;padding-top:70px}
.why-grid{display:flex;justify-content:space-between;margin-top:60px}
.why-text{width:520px;font-size:14px;line-height:20px;color:#333}
.why-text ul{list-style:none;margin-top:24px}
.why-text li{line-height:28px;display:flex;align-items:center;gap:10px}
.why-text li::before{content:"";width:8px;height:8px;background:var(--ink);border-radius:50%}
.why-text .btn{margin-top:20px}
.why .photo{width:517px;height:345px;background:linear-gradient(135deg,#dfe9ef,#f6f8f9 50%,#c7d8e2)}

/* testimonials */
.testimonials{height:466px;background:linear-gradient(90deg,#3b3e42,#55585c 50%,#393b3e);position:relative;padding-top:80px;color:var(--white);text-align:center}
.testimonials .section-title{color:var(--white)}
.quote{width:980px;margin:24px auto 0;font-size:15px;font-weight:600;line-height:26px}
.quote cite{display:block;font-style:normal;margin-top:4px}
.t-arrow{position:absolute;top:250px}
.t-arrow.left{left:60px}.t-arrow.right{right:60px}

/* team */
.team{height:622px;padding-top:66px}
.team-row{display:flex;justify-content:space-between;margin-top:74px}
.member{width:320px;text-align:center}
.member .photo{height:304px;background:linear-gradient(180deg,#dde7ee,#f4f6f7 60%,#e3eaef)}
.member h4{font-size:18px;font-weight:700;margin-top:16px}
.member p{font-size:15px;color:var(--muted);margin-top:4px}

/* footer */
.footer{height:300px;background:var(--blue);color:var(--white);padding-top:52px}
.footer .wrap{display:flex}
.f-col{flex:none}
.f-about{width:370px;margin-right:50px}
.f-contact{width:356px;margin-right:50px}
.f-hours{width:258px}
.f-col h5{font-size:20px;font-weight:700;margin-bottom:16px}
.f-col p{font-size:13px;line-height:22px;font-weight:600}
.copyright{height:74px;background:#111;color:var(--white);font-size:13px;font-weight:600;text-align:center;line-height:74px}
</style>
</head>
<body>

<div class="topbar">
  <div class="wrap">
    <div>Telephone : + 11 (0)20 4400 0022</div>
    <div class="social" aria-label="Social media links"><span></span><span></span><span></span></div>
  </div>
</div>

<header class="header">
  <div class="wrap">
    <div class="brand">FERNLY<small>MEDICAL CLINIC</small></div>
    <nav class="nav"><span>HOME</span><span>ABOUT US</span><span>SERVICES</span><span>TESTIMONIALS</span><span>BLOG</span><span>CONTACT</span></nav>
    <div class="cta">SCHEDULE AN APPOINTMENT</div>
  </div>
</header>

<section class="hero" role="img" aria-label="Hero photo of a doctor with stethoscope and clipboard beside a patient">
  <div class="arrow left"><svg width="16" height="28" viewBox="0 0 16 28"><path d="M14 2L3 14l11 12" stroke="#fff" stroke-width="4" fill="none"/></svg></div>
  <div class="hero-text">
    <h1>Welcome to<br>Fernly Medical Clinic</h1>
    <p>Lorem Ipsum is simply dummy text of the printing and typesetting industry. Lorem Ipsum</p>
  </div>
  <div class="arrow right"><svg width="16" height="28" viewBox="0 0 16 28"><path d="M2 2l11 12L2 26" stroke="#fff" stroke-width="4" fill="none"/></svg></div>
</section>

<section class="services">
  <div class="wrap">
    <h2 class="section-title">Our Services</h2>
    <div class="service-row">
      <div class="service">
        <div class="icon"><svg width="60" height="60" viewBox="0 0 60 60" fill="none" stroke="#fff" stroke-width="3"><ellipse cx="30" cy="30" rx="26" ry="10"/><ellipse cx="30" cy="30" rx="26" ry="10" transform="rotate(60 30 30)"/><ellipse cx="30" cy="30" rx="26" ry="10" transform="rotate(-60 30 30)"/><circle cx="30" cy="30" r="4" fill="#fff"/></svg></div>
        <div class="service-card"><h3>Lorem Ipsum is simply</h3><p>Lorem Ipsum is simply dummy text of the printing and typesetting industry. Lorem Ipsum has been the</p><span class="btn">Read More</span></div>
      </div>
      <div class="service">
        <div class="icon"><svg width="64" height="56" viewBox="0 0 64 56" fill="none" stroke="#fff" stroke-width="4"><path d="M32 52S4 34 4 17A13 13 0 0 1 32 11a13 13 0 0 1 28 6c0 17-28 35-28 35z"/><path d="M10 28h12l5-9 6 16 5-7h16" stroke-width="3"/></svg></div>
        <div class="service-card"><h3>Lorem Ipsum is simply</h3><p>Lorem Ipsum is simply dummy text of the printing and typesetting industry. Lorem Ipsum has been the industry's standard dummy</p><span class="btn">Read More</span></div>
      </div>
      <div class="service">
        <div class="icon"><svg width="60" height="60" viewBox="0 0 60 60" fill="none" stroke="#fff" stroke-width="4" stroke-linecap="round"><circle cx="38" cy="10" r="5" fill="#fff"/><path d="M22 22l12-4 6 12 10 2M34 18l-6 16 10 8v12M28 34l-8 10H10"/><path d="M6 14h10M4 22h10" stroke-width="3"/></svg></div>
        <div class="service-card"><h3>Lorem Ipsum is simply</h3><p>Lorem Ipsum is simply dummy text of the printing and typesetting industry. Lorem Ipsum has been the industry's standard dummy</p><span class="btn">Read More</span></div>
      </div>
      <div class="service">
        <div class="icon"><svg width="60" height="60" viewBox="0 0 60 60" fill="none" stroke="#fff" stroke-width="4" stroke-linecap="round"><circle cx="20" cy="14" r="6" fill="#fff"/><path d="M12 26h18l10 14h10M16 26v18h18M6 52h48M20 44v8M44 44v8"/></svg></div>
        <div class="service-card"><h3>Lorem Ipsum is simply</h3><p>Lorem Ipsum is simply dummy text of the printing and typesetting industry. Lorem Ipsum has been the industry's standard dummy</p><span class="btn">Read More</span></div>
      </div>
    </div>
  </div>
</section>

<section class="expect">
  <div class="wrap">
    <h2 class="section-title">What to Expect</h2>
    <div class="faq">
      <h4>Heare Is Headline</h4>
      <p>Lorem Ipsum is simply dummy text of the printing and typesetting industry. Lorem Ipsum has been the industry's standard dummy text ever since the 1500s, when an unknown printer took a galley of type and scrambled it to make a type specimen book.</p>
      <h4>Heare Is Headline</h4>
      <p>Lorem Ipsum is simply dummy text of the printing and typesetting industry. Lorem Ipsum has been the industry's standard dummy text ever since the 1500s, when an unknown printer took a galley of type and scrambled it to make a type specimen book.</p>
      <h4>Heare Is Headline</h4>
      <p>Lorem Ipsum is simply dummy text of the printing and typesetting industry. Lorem Ipsum has been the industry's standard dummy text ever since the 1500s, when an unknown printer took a galley of type and scrambled it to make a type specimen book.</p>
    </div>
  </div>
  <div class="photo" role="img" aria-label="Portrait photo of a smiling female doctor in a white coat with stethoscope"></div>
</section>

<section class="blog">
  <div class="wrap">
    <h2 class="section-title">Our Recent Blog Posts</h2>
    <div class="blog-row">
      <article class="post"><div class="photo" role="img" aria-label="Photo of a doctor talking with a patient"></div><div class="post-body"><h3>Meet the Doc</h3><p>Dr. YOU I want to start off with a disclaimer. I'm not sure if you can tell from the thick glasses or not, but... I'm a huge nerd that specializes as a chiropractor. Anyone else like me? Any other nerds? ...... Ok so a few of us. Well, in my opinion, being a nerd...</p><span class="more">Read More</span></div></article>
      <article class="post"><div class="photo" role="img" aria-label="Photo of a doctor talking with a patient"></div><div class="post-body"><h3>Meet the Doc</h3><p>Dr. YOU I want to start off with a disclaimer. I'm not sure if you can tell from the thick glasses or not, but... I'm a huge nerd that specializes as a chiropractor. Anyone else like me? Any other nerds? ...... Ok so a few of us. Well, in my opinion, being a nerd...</p><span class="more">Read More</span></div></article>
      <article class="post"><div class="photo" role="img" aria-label="Photo of a doctor talking with a patient"></div><div class="post-body"><h3>Meet the Doc</h3><p>Dr. YOU I want to start off with a disclaimer. I'm not sure if you can tell from the thick glasses or not, but... I'm a huge nerd that specializes as a chiropractor. Anyone else like me? Any other nerds? ...... Ok so a few of us. Well, in my opinion, being a nerd...</p><span class="more">Read More</span></div></article>
    </div>
  </div>
</section>

<section class="why">
  <div class="wrap">
    <h2 class="section-title">Why Choose Us?</h2>
    <div class="why-grid">
      <div class="why-text">
        <p>We are health care professionals composed of a variety of physicians and therapists that are experts in posture and structural correction of the spine.</p>
        <ul>
          <li>Why choose Sentence why choose Sentence</li>
          <li>Why choose Sentence why choose Sentence</li>
          <li>Why choose Sentence why choose Sentence</li>
          <li>Why choose Sentence why choose Sentence</li>
          <li>Why choose Sentence why choose Sentence</li>
          <li>Why choose Sentence why choose Sentence</li>
          <li>Why choose Sentence why choose Sentence</li>
        </ul>
        <span class="btn">Read More</span>
      </div>
      <div class="photo" role="img" aria-label="Photo of a dentist and assistant with a child patient"></div>
    </div>
  </div>
</section>

<section class="testimonials" role="group" aria-label="Testimonials over a dimmed clinic photo">
  <h2 class="section-title">What Pepole Are Saying</h2>
  <p class="quote">Lorem Ipsum is simply dummy text of the printing and typesetting industry. Lorem Ipsum has been the industry's standard dummy text ever since the 1500s, when an unknown printer took a galley of type and scrambled it to make a type specimen book. Lorem Ipsum is simply dummy text of the printing and typesetting industry. Lorem Ipsum has been the industry's standard dummy text ever since the 1500s, when an unknown printer took a galley of type and scrambled it to make a type specimen book.<cite>-xyperson</cite></p>
  <svg class="t-arrow left" width="24" height="44" viewBox="0 0 24 44"><path d="M20 3L5 22l15 19" stroke="#fff" stroke-width="6" fill="none"/></svg>
  <svg class="t-arrow right" width="24" height="44" viewBox="0 0 24 44"><path d="M4 3l15 19L4 41" stroke="#fff" stroke-width="6" fill="none"/></svg>
</section>

<section class="team">
  <div class="wrap">
    <h2 class="section-title">Meet Our Team</h2>
    <div class="team-row">
      <div class="member"><div class="photo" role="img" aria-label="Portrait photo of a male doctor with stethoscope"></div><h4>Dr. Elan Porter</h4><p>Pediatrist</p></div>
      <div class="member"><div class="photo" role="img" aria-label="Portrait photo of a male doctor with stethoscope"></div><h4>Dr. Elan Porter</h4><p>Pediatrist</p></div>
      <div class="member"><div class="photo" role="img" aria-label="Portrait photo of a male doctor with stethoscope"></div><h4>Dr. Elan Porter</h4><p>Pediatrist</p></div>
    </div>
  </div>
</section>

<footer class="footer">
  <div class="wrap">
    <div class="f-col f-about"><h5>About Fernly</h5><p>Lorem Ipsum is simply dummy text of the printing and typesetting industry. Lorem Ipsum has been the industry's standard dummy text ever since the 1500s, when an unknown printer took a galley of type and scrambled it to make a type specimen book.</p></div>
    <div class="f-col f-contact"><h5>Contact&nbsp; With Us</h5><p>Lorem Ipsum Street lorem, NTC 6AG<br>Lorem Ispum City<br>Telephone : + 11 (0)20 4400 0022<br>Email : info@fernlyclinic.example</p></div>
    <div class="f-col f-hours"><h5>Our Hours</h5><p>Monday: 10am - 1pm &amp; 3pm - 7pm<br>Tuesday: 10am - 1pm &amp; 3pm - 7pm<br>Wednesday:10am - 1pm &amp; 3pm - 7pm<br>Thursday:10am - 1pm &amp; 3pm - 7pm<br>Friday: 10am - 1pm &amp; 3pm - 7pm<br>Closed: Saturday &amp; Sunday</p></div>
  </div>
</footer>
<div class="copyright">Copyright 2017 All Reight Reserved Fernly Medical Clinic</div>

</body>
</html>
```